Swim School Certificates

We are looking to have some certificates designed for our Learn to Swim School. These will be handed out to our students when they complete each level. We will need different certificates for each level, however, we would like a consistent theme throughout, so each level may only have a slight variation. We are happy for you to just show us a couple of variations to begin with, so we can see how these would work. Then once we decide on the winning design, you can complete the rest.
The levels are:
Bubs 1
Bubs 2
Toddler 1
Toddler 2
Beginner 1
Beginner 2
Beginner 3
Stroke Development 1
Stroke Development 2
Advanced 1
Advanced 2
Squad
The Certificates should include:
Congratulations to:
(blank line for name)
You have completed (level name), Keep up the good work!!!
Signed: (blank line) Date: (blank line)
I've included a copy of our logo, and a copy of our governing bodies logo both of which should be included on the certificate.
I've also included some examples of certificates we like, to give you an idea of our style. We are happy for the bubs and toddler certificates to be more child focused, so they can included a kid friendly element to them, however this will need to reduce to a more simplistic design as the levels increase into beginner and stroke etc.
You can also look on our Facebook page to get an idea of what we do.
https://www.facebook.com/coralreefswimschool/?ref=bookmarks
We will also need editable source files upon completion as we may be looking to change the name of some classes in the future.
Please let us know if you need any of the files in other formats
Kind Regards
Maree

```html
<!DOCTYPE html>
<html lang="en">
<head>
<meta charset="UTF-8">
<title>Swim School Level Certificates</title>
<link rel="stylesheet" href="https://fonts.googleapis.com/css2?family=Chewy&family=Dosis:wght@600;700&family=Open+Sans:wght@700;800&display=swap">
<style>
  :root {
    --page-bg: #e4e4e4;
    --card-bg: #ffffff;
    --card-shade: #ececec;
    --frame-blue: #2f78c4;
    --frame-light: #8cc6f0;
    --water-deep: #1f6cc0;
    --water-mid: #2f7fd0;
    --title-red: #e0202a;
    --level-blue: #2c7fd2;
    --line-blue: #6aa8dc;
    --text-dark: #3a3a3a;
    --ring-red: #e0202a;
    --ring-grey: #dcdcdc;
    --skin: #f4cfa8;
  }
  * { box-sizing: border-box; margin: 0; padding: 0; }
  html, body { width: 1200px; height: 1200px; overflow: hidden; }
  body { background: var(--page-bg); position: relative; font-family: "Open Sans", Arial, sans-serif; }

  .certificate {
    position: absolute;
    width: 544px; height: 386px;
    background: radial-gradient(ellipse at 50% 40%, var(--card-bg) 55%, var(--card-shade) 100%);
    overflow: hidden;
    box-shadow: 0 4px 14px rgba(0,0,0,0.18);
  }
  .certificate--bubs-1 { left: 34px; top: 261px; }
  .certificate--bubs-2 { left: 629px; top: 258px; }
  .certificate--toddler-1 { left: 357px; top: 696px; }

  .certificate__border, .certificate__water { position: absolute; left: 0; top: 0; }

  .certificate__swimmer {
    position: absolute; left: 70px; top: 127px;
    width: 68px; height: 148px;
    border-radius: 30px 30px 8px 8px;
    background: linear-gradient(180deg, #e9a84a 0%, #8cc6f0 18%, var(--skin) 30%, var(--skin) 58%, #3a8fe0 62%, #3a8fe0 75%, var(--skin) 78%);
  }

  .certificate__title {
    position: absolute; left: 0; right: 0; top: 76px;
    text-align: center; padding-left: 20px;
    font-family: "Chewy", "Comic Sans MS", sans-serif;
    font-weight: 400;
    font-size: 31px; line-height: 38px; letter-spacing: 1px;
    color: var(--title-red);
    text-transform: uppercase;
  }

  .field {
    position: absolute; display: flex; align-items: flex-end;
    font-size: 12px; line-height: 16px; font-weight: 800; color: var(--text-dark);
  }
  .field__line { display: inline-block; border-bottom: 1.5px solid var(--line-blue); margin-left: 12px; margin-bottom: 3px; }
  .field--name { left: 156px; top: 122px; text-transform: uppercase; font-size: 11px; }
  .field--name .field__line { width: 204px; }
  .field--date { left: 156px; top: 214px; }
  .field--date .field__line { width: 80px; }
  .field--signed { left: 322px; top: 214px; }
  .field--signed .field__line { width: 80px; }

  .completed {
    position: absolute; left: 156px; top: 146px;
    display: flex; align-items: baseline;
    font-size: 11px; line-height: 24px; font-weight: 700; color: var(--text-dark);
  }
  .completed__level {
    font-family: "Dosis", sans-serif; font-weight: 700;
    font-size: 20px; color: var(--level-blue); margin-left: 8px;
    text-transform: uppercase;
  }

  .encouragement {
    position: absolute; left: 156px; top: 170px;
    display: flex; align-items: center; gap: 10px;
    font-family: "Chewy", "Comic Sans MS", sans-serif; font-size: 22px; line-height: 30px;
    color: var(--title-red);
  }
  .encouragement__icon { width: 30px; height: 30px; flex: none; }

  .lifering {
    position: absolute; border-radius: 50%;
    background: radial-gradient(circle, #f3f3f3 45%, var(--ring-grey) 70%, #e88a8e 100%);
  }
  .lifering--partner { left: 261px; top: 258px; width: 90px; height: 90px; }
  .lifering--school { left: 371px; top: 251px; width: 104px; height: 104px; }

  .badge-partner {
    position: absolute; left: 284px; top: 281px; width: 44px; height: 44px;
    border-radius: 50%; background: var(--frame-light);
  }
  .school-name {
    position: absolute; left: 383px; top: 292px; width: 80px;
    text-align: center; line-height: 22px;
    font-family: "Dosis", sans-serif; font-weight: 700; font-size: 15px;
    color: var(--level-blue);
  }
</style>
</head>
<body>

<section class="certificate certificate--bubs-1" aria-label="Bubs 1 certificate">
  <svg class="certificate__border" width="544" height="386" role="img" aria-label="Bubble border framing the certificate">
    <defs><linearGradient id="border-tone-1" x1="0" y1="0" x2="1" y2="1"><stop offset="0" stop-color="#3f8ad4"/><stop offset="1" stop-color="#7dbcec"/></linearGradient></defs>
    <path fill-rule="evenodd" fill="url(#border-tone-1)" d="M18 44 Q18 18 44 18 L514 18 Q540 18 540 44 L540 330 L18 330 Z M58 62 L502 62 L502 330 L58 330 Z"/>
  </svg>
  <svg class="certificate__water" width="544" height="386" role="img" aria-label="Splashing pool water">
    <path d="M0 285 C60 276 120 290 180 280 C230 268 250 250 280 258 C320 266 360 276 420 268 C470 262 510 272 544 264 L544 386 L0 386 Z" fill="var(--water-mid)"/>
    <path d="M0 312 C90 300 200 322 300 310 C400 298 480 316 544 304 L544 386 L0 386 Z" fill="var(--water-deep)"/>
  </svg>
  <div class="certificate__swimmer" role="img" aria-label="Illustration of a young swimmer in goggles and snorkel"></div>
  <h2 class="certificate__title">Congratulations to</h2>
  <p class="field field--name">Name<span class="field__line"></span></p>
  <p class="completed">You have completed<span class="completed__level">Bubs 1</span></p>
  <p class="encouragement">Keep up the good work
    <svg class="encouragement__icon" viewBox="0 0 30 30"><circle cx="15" cy="15" r="13" fill="#fff" stroke="var(--frame-blue)" stroke-width="3"/><circle cx="15" cy="15" r="8" fill="var(--frame-blue)"/><path d="M11 15 l3 3 l5 -6" fill="none" stroke="#fff" stroke-width="2.2"/></svg>
  </p>
  <p class="field field--date">Date<span class="field__line"></span></p>
  <p class="field field--signed">Signed<span class="field__line"></span></p>
  <div class="lifering lifering--partner" role="img" aria-label="Life ring illustration"></div>
  <div class="badge-partner" role="img" aria-label="Governing body badge"></div>
  <div class="lifering lifering--school" role="img" aria-label="Life ring illustration"></div>
  <span class="school-name">Coral Reef</span>
</section>

<section class="certificate certificate--bubs-2" aria-label="Bubs 2 certificate">
  <svg class="certificate__border" width="544" height="386" role="img" aria-label="Bubble border framing the certificate">
    <defs><linearGradient id="border-tone-2" x1="0" y1="0" x2="1" y2="1"><stop offset="0" stop-color="#3f8ad4"/><stop offset="1" stop-color="#7dbcec"/></linearGradient></defs>
    <path fill-rule="evenodd" fill="url(#border-tone-2)" d="M18 44 Q18 18 44 18 L514 18 Q540 18 540 44 L540 330 L18 330 Z M58 62 L502 62 L502 330 L58 330 Z"/>
  </svg>
  <svg class="certificate__water" width="544" height="386" role="img" aria-label="Splashing pool water">
    <path d="M0 285 C60 276 120 290 180 280 C230 268 250 250 280 258 C320 266 360 276 420 268 C470 262 510 272 544 264 L544 386 L0 386 Z" fill="var(--water-mid)"/>
    <path d="M0 312 C90 300 200 322 300 310 C400 298 480 316 544 304 L544 386 L0 386 Z" fill="var(--water-deep)"/>
  </svg>
  <div class="certificate__swimmer" role="img" aria-label="Illustration of a young swimmer in goggles and snorkel"></div>
  <h2 class="certificate__title">Congratulations to</h2>
  <p class="field field--name">Name<span class="field__line"></span></p>
  <p class="completed">You have completed<span class="completed__level">Bubs 2</span></p>
  <p class="encouragement">Keep up the good work
    <svg class="encouragement__icon" viewBox="0 0 30 30"><circle cx="15" cy="15" r="13" fill="#fff" stroke="var(--frame-blue)" stroke-width="3"/><circle cx="15" cy="15" r="8" fill="var(--frame-blue)"/><path d="M11 15 l3 3 l5 -6" fill="none" stroke="#fff" stroke-width="2.2"/></svg>
  </p>
  <p class="field field--date">Date<span class="field__line"></span></p>
  <p class="field field--signed">Signed<span class="field__line"></span></p>
  <div class="lifering lifering--partner" role="img" aria-label="Life ring illustration"></div>
  <div class="badge-partner" role="img" aria-label="Governing body badge"></div>
  <div class="lifering lifering--school" role="img" aria-label="Life ring illustration"></div>
  <span class="school-name">Coral Reef</span>
</section>

<section class="certificate certificate--toddler-1" aria-label="Toddler 1 certificate">
  <svg class="certificate__border" width="544" height="386" role="img" aria-label="Bubble border framing the certificate">
    <defs><linearGradient id="border-tone-3" x1="0" y1="0" x2="1" y2="1"><stop offset="0" stop-color="#3f8ad4"/><stop offset="1" stop-color="#7dbcec"/></linearGradient></defs>
    <path fill-rule="evenodd" fill="url(#border-tone-3)" d="M18 44 Q18 18 44 18 L514 18 Q540 18 540 44 L540 330 L18 330 Z M58 62 L502 62 L502 330 L58 330 Z"/>
  </svg>
  <svg class="certificate__water" width="544" height="386" role="img" aria-label="Splashing pool water">
    <path d="M0 285 C60 276 120 290 180 280 C230 268 250 250 280 258 C320 266 360 276 420 268 C470 262 510 272 544 264 L544 386 L0 386 Z" fill="var(--water-mid)"/>
    <path d="M0 312 C90 300 200 322 300 310 C400 298 480 316 544 304 L544 386 L0 386 Z" fill="var(--water-deep)"/>
  </svg>
  <div class="certificate__swimmer" role="img" aria-label="Illustration of a young swimmer in goggles and snorkel"></div>
  <h2 class="certificate__title">Congratulations to</h2>
  <p class="field field--name">Name<span class="field__line"></span></p>
  <p class="completed">You have completed<span class="completed__level">Toddler 1</span></p>
  <p class="encouragement">Keep up the good work
    <svg class="encouragement__icon" viewBox="0 0 30 30"><circle cx="15" cy="15" r="13" fill="#fff" stroke="var(--frame-blue)" stroke-width="3"/><circle cx="15" cy="15" r="8" fill="var(--frame-blue)"/><path d="M11 15 l3 3 l5 -6" fill="none" stroke="#fff" stroke-width="2.2"/></svg>
  </p>
  <p class="field field--date">Date<span class="field__line"></span></p>
  <p class="field field--signed">Signed<span class="field__line"></span></p>
  <div class="lifering lifering--partner" role="img" aria-label="Life ring illustration"></div>
  <div class="badge-partner" role="img" aria-label="Governing body badge"></div>
  <div class="lifering lifering--school" role="img" aria-label="Life ring illustration"></div>
  <span class="school-name">Coral Reef</span>
</section>

</body>
</html>
```